Business cards and stationery for a software company
Klovarent s.r.o.
Simple
Petr Hrubeš
Lipová alej 2841/9
Praha 5
petr.hrubes@klovarent-example.com
www.klovarent-example.com

```html
<!DOCTYPE html>
<html lang="cs">
<head>
<meta charset="utf-8">
<title>Klovarent s.r.o. – vizitka</title>
<link href="https://fonts.googleapis.com/css2?family=Open+Sans:wght@400;600;700;800&display=swap" rel="stylesheet">
<style>
  :root {
    --bg: #e9e6ec;
    --card: #ffffff;
    --purple: #7b4f9e;
    --purple-dark: #5e3a80;
    --ink: #231f20;
    --white: #ffffff;
  }
  html, body {
    margin: 0;
    width: 1200px;
    height: 914px;
    overflow: hidden;
    background: var(--bg);
    font-family: "Open Sans", Arial, sans-serif;
  }
  .business-card {
    position: absolute;
    left: 100px;
    top: 171px;
    width: 1000px;
    height: 572px;
    background: var(--card);
    box-shadow: 0 10px 30px rgba(40, 20, 60, 0.18);
    overflow: hidden;
  }
  .card-shapes {
    position: absolute;
    inset: 0;
  }
  .brand {
    position: absolute;
    left: 80px;
    top: 70px;
    display: flex;
    align-items: center;
    gap: 16px;
  }
  .brand-dot {
    width: 52px;
    height: 52px;
    border-radius: 50%;
    background: var(--purple);
  }
  .brand-name {
    font-size: 56px;
    font-weight: 800;
    color: var(--purple);
    letter-spacing: -1px;
    line-height: 1;
  }
  .person-name {
    position: absolute;
    left: 80px;
    top: 232px;
    margin: 0;
    font-size: 26px;
    font-weight: 700;
    color: var(--purple);
  }
  .address {
    position: absolute;
    left: 40px;
    top: 398px;
    margin: 0;
    font-size: 19px;
    color: var(--white);
    white-space: nowrap;
  }
  .contacts {
    position: absolute;
    left: 640px;
    top: 436px;
    margin: 0;
    padding: 0;
    list-style: none;
  }
  .contacts li {
    display: flex;
    align-items: center;
    gap: 12px;
    height: 34px;
    font-size: 18px;
    color: var(--white);
    white-space: nowrap;
  }
  .contact-icon {
    width: 22px;
    height: 22px;
    flex: none;
  }
</style>
</head>
<body>
  <div class="business-card">
    <svg class="card-shapes" viewBox="0 0 1000 572" width="1000" height="572" aria-hidden="true">
      <defs>
        <linearGradient id="bandGradient" x1="0" y1="0" x2="1" y2="1">
          <stop offset="0" stop-color="#6a4190"/>
          <stop offset="0.55" stop-color="#8a5db0"/>
          <stop offset="1" stop-color="#6b4292"/>
        </linearGradient>
      </defs>
      <path class="purple-band" d="M0,318 C250,398 620,430 1000,292 L1000,572 L0,572 Z" fill="url(#bandGradient)"/>
      <path class="swoosh" d="M0,290 C250,370 600,400 1000,250 C620,414 250,384 0,302 Z" fill="#231f20"/>
    </svg>

    <div class="brand">
      <span class="brand-dot"></span>
      <span class="brand-name">Klovarent</span>
    </div>

    <p class="person-name">Petr Hrubeš</p>

    <p class="address">Lipová alej 2841/9 Praha 5</p>

    <ul class="contacts">
      <li>
        <svg class="contact-icon" viewBox="0 0 22 22"><circle cx="11" cy="11" r="11" fill="#fff"/><path d="M7.5 5.5l2 2-1 1.5c.8 1.6 2 2.8 3.5 3.5l1.5-1 2 2-1.2 1.8c-3.8-.6-7.4-4.2-8-8z" fill="#7b4f9e"/></svg>
        +420 700 555 012
      </li>
      <li>
        <svg class="contact-icon" viewBox="0 0 22 22"><circle cx="11" cy="11" r="11" fill="#fff"/><rect x="5.5" y="7" width="11" height="8" fill="none" stroke="#7b4f9e" stroke-width="1.5"/><path d="M5.5 7l5.5 4.5L16.5 7" fill="none" stroke="#7b4f9e" stroke-width="1.5"/></svg>
        petr.hrubes@klovarent-example.com
      </li>
      <li>
        <svg class="contact-icon" viewBox="0 0 22 22"><circle cx="11" cy="11" r="11" fill="#fff"/><circle cx="11" cy="11" r="5.5" fill="none" stroke="#7b4f9e" stroke-width="1.4"/><path d="M5.5 11h11M11 5.5c-2.5 3-2.5 8 0 11M11 5.5c2.5 3 2.5 8 0 11" fill="none" stroke="#7b4f9e" stroke-width="1.2"/></svg>
        www.klovarent-example.com
      </li>
    </ul>
  </div>
</body>
</html>
```